Whitmore Business Card Design

The name of the business is Dara Whitmore, CPA LLC
The service that we offer is Accounting, Tax & Consulting Services. I need it to have the following items:
Dara Whitmore, Principal
Phone Number
Email Address
Physical Address

I have attached the company logo, one in black and one in white. Please provide a design in black background and the other in white background. Please include "Accounting, Tax & Consulting Services". I want the business card to be clean and very professional.

```html
<!DOCTYPE html>
<html lang="en">
<head>
<meta charset="utf-8">
<title>Dara Whitmore, CPA LLC — Business Card</title>
<link rel="stylesheet" href="https://fonts.googleapis.com/css2?family=Montserrat:wght@500;600;700&family=Arimo:wght@400;700&display=swap">
<style>
  :root {
    --page-bg: #e4e4e4;
    --card-white: #ffffff;
    --card-dark: #3b3b3e;
    --brand-red: #9b1b20;
    --ink: #333336;
    --ink-soft: #6f6f72;
    --rule: #a9a9ad;
    --on-dark: #ffffff;
    --on-dark-soft: #a6a6aa;
  }
  * { box-sizing: border-box; margin: 0; padding: 0; }
  html, body { width: 1200px; height: 802px; overflow: hidden; }
  body {
    background: var(--page-bg);
    position: relative;
    font-family: "Arimo", Arial, sans-serif;
  }
  .card {
    position: absolute;
    width: 560px;
    height: 320px;
    overflow: hidden;
    box-shadow: 0 10px 24px rgba(0,0,0,0.18);
  }
  /* Front */
  .card--front { left: 60px; top: 60px; background: var(--card-white); }
  .card__wave { position: absolute; inset: 0; width: 100%; height: 100%; }
  .brand {
    position: absolute; left: 28px; top: 116px;
    display: flex; align-items: center; gap: 9px;
  }
  .brand__mark { width: 13px; height: 13px; background: var(--brand-red); flex: none; }
  .brand__name {
    font-family: "Montserrat", sans-serif;
    font-weight: 600; font-size: 14px; letter-spacing: 0.03em;
    color: var(--ink); text-transform: uppercase; white-space: nowrap;
  }
  .brand__tagline {
    position: absolute; left: 50px; top: 138px;
    font-family: "Montserrat", sans-serif; font-weight: 500;
    font-size: 8px; letter-spacing: 0.16em; color: var(--ink-soft);
    text-transform: uppercase; white-space: nowrap;
  }
  .divider {
    position: absolute; left: 292px; top: 50px;
    width: 1px; height: 136px; background: var(--rule);
  }
  .contact { position: absolute; left: 310px; top: 44px; color: var(--ink); }
  .contact__name {
    font-family: "Arimo", Arial, sans-serif; font-weight: 700;
    font-size: 21px; color: var(--brand-red); text-transform: uppercase;
    letter-spacing: 0.01em; line-height: 1;
  }
  .contact__title { font-size: 12px; margin-top: 4px; }
  .contact__address { font-size: 12px; line-height: 1.3; margin-top: 12px; }
  .contact__list { list-style: none; margin-top: 10px; font-size: 12px; line-height: 1.45; }
  .contact__list li { display: flex; align-items: center; gap: 8px; }
  .contact__icon { width: 11px; height: 11px; flex: none; }
  /* Back */
  .card--back { left: 580px; top: 420px; background: var(--card-dark); }
  .back-brand { position: absolute; left: 0; right: 0; top: 96px; text-align: center; }
  .back-brand__name {
    font-family: "Montserrat", sans-serif; font-weight: 600;
    font-size: 22px; letter-spacing: 0.05em; color: var(--on-dark);
    text-transform: uppercase;
  }
  .back-brand__tagline {
    margin-top: 6px;
    font-family: "Montserrat", sans-serif; font-weight: 500;
    font-size: 12px; letter-spacing: 0.2em; color: var(--on-dark-soft);
    text-transform: uppercase;
  }
  .services {
    position: absolute; left: 0; right: 0; bottom: 70px; text-align: center;
    font-size: 17px; color: var(--on-dark); letter-spacing: 0.01em;
  }
</style>
</head>
<body>

<section class="card card--front" aria-label="Business card, front">
  <svg class="card__wave" viewBox="0 0 560 320" preserveAspectRatio="none" aria-hidden="true">
    <path d="M0,280 C150,284 270,258 372,222 C272,266 150,296 0,300 Z" fill="var(--ink)"/>
    <path d="M0,304 C150,300 280,272 380,240 C450,220 500,224 560,214 L560,320 L0,320 Z"
          fill="var(--brand-red)"/>
  </svg>

  <div class="brand">
    <span class="brand__mark"></span>
    <span class="brand__name">Dara Whitmore, CPA LLC</span>
  </div>
  <p class="brand__tagline">Certified Public Accountant</p>

  <div class="divider"></div>

  <div class="contact">
    <p class="contact__name">Dara Whitmore</p>
    <p class="contact__title">Principal</p>
    <p class="contact__address">Your address, city<br>state, ZIP 0000</p>
    <ul class="contact__list">
      <li>
        <svg class="contact__icon" viewBox="0 0 12 12" aria-hidden="true"><path d="M2.5 1 L4.5 1 L5.2 3.4 L4 4.4 C4.6 5.8 6 7.3 7.6 8 L8.6 6.8 L11 7.5 L11 9.5 C11 10.3 10.3 11 9.5 11 C5 11 1 7 1 2.5 C1 1.7 1.7 1 2.5 1 Z" fill="var(--brand-red)"/></svg>
        <span>555-014-2100</span>
      </li>
      <li>
        <svg class="contact__icon" viewBox="0 0 12 12" aria-hidden="true"><rect x="1" y="2.5" width="10" height="7" fill="none" stroke="var(--brand-red)" stroke-width="1.2"/><path d="M1 2.5 L6 6.5 L11 2.5" fill="none" stroke="var(--brand-red)" stroke-width="1.2"/></svg>
        <span>dara@whitmorecpa.com</span>
      </li>
      <li>
        <svg class="contact__icon" viewBox="0 0 12 12" aria-hidden="true"><circle cx="6" cy="6" r="5" fill="var(--brand-red)"/><path d="M1 6 H11 M6 1 C3.5 3.5 3.5 8.5 6 11 M6 1 C8.5 3.5 8.5 8.5 6 11" fill="none" stroke="#fff" stroke-width="0.8"/></svg>
        <span>www.whitmorecpa.com</span>
      </li>
    </ul>
  </div>
</section>

<section class="card card--back" aria-label="Business card, back">
  <div class="back-brand">
    <p class="back-brand__name">Dara Whitmore, CPA LLC</p>
    <p class="back-brand__tagline">Certified Public Accountant</p>
  </div>
  <p class="services">Accounting, Tax &amp; Consulting Services</p>
</section>

</body>
</html>
```